Beauty Salon Design

The business card design will be for a new beauty salon opening up.

The therapist has over 11 years at a leading beauty Salon in perth.

The two colours that the salon will use is black and gold.

Industry/Entity Type

Beauty Salon

Contact Information for Business Card

Lumora Beauty

Corinne Halstead Pryce
Advanced beauty therapist
0455 817 302

Monday - Friday 9am - 2.30pm
Weekends and nights by appointment only

Waxing, Tinting, Swedish massage, hot stone massage, facials, peels, micro, LED light treatment, skin needling and retail products.

```html
<!DOCTYPE html>
<html lang="es">
<head>
<meta charset="utf-8">
<title>Lumora Beauty – Business Card</title>
<link href="https://fonts.googleapis.com/css2?family=Roboto+Condensed:wght@300;400&display=swap" rel="stylesheet">
<style>
  :root {
    --gold: #c9a13a;
    --gold-light: #f2d27a;
    --gold-deep: #b8862a;
    --black: #050505;
    --slate: #2d363c;
    --white: #ffffff;
    --ink: #2b2b2b;
    --text-dark: #2a2a2a;
    --silver: #dcdcdc;
    --grey-line: #6f6f6f;
  }
  * { margin: 0; padding: 0; box-sizing: border-box; }
  html, body { width: 966px; height: 1200px; overflow: hidden; background: var(--white); }
  body { font-family: "Roboto Condensed", "Arial Narrow", sans-serif; font-weight: 300; position: relative; }

  .card { position: absolute; left: 0; width: 966px; overflow: hidden; }
  .card-front { top: 0; height: 596px; background: var(--slate); }
  .card-back { top: 603px; height: 597px; }

  .front-photo {
    position: absolute; left: 0; top: 0; width: 480px; height: 596px;
    background:
      radial-gradient(ellipse at 70% 55%, #a9714b 0%, #7a4c30 30%, rgba(60,40,30,0) 62%),
      linear-gradient(160deg, #3a3f43 0%, #2a2c2e 40%, #1d1a18 100%);
  }
  .card-shapes { position: absolute; left: 0; top: 0; }

  .services-title {
    position: absolute; left: 492px; top: 52px;
    font-size: 22px; color: var(--gold); letter-spacing: 0.5px; font-weight: 300;
  }
  .services-list {
    position: absolute; top: 96px; list-style: none;
    font-size: 23.5px; line-height: 30.5px; color: var(--ink); font-weight: 300;
  }
  .services-list li { position: relative; padding-left: 12px; }
  .services-list li::before {
    content: ""; position: absolute; left: 0; top: 13px;
    width: 5px; height: 5px; border-radius: 50%; background: var(--gold);
  }
  .services-list .wrap { display: block; padding-left: 0; }
  .services-left { left: 493px; }
  .services-right { left: 626px; }

  .therapist-name {
    position: absolute; left: 529px; top: 358px;
    font-size: 29.5px; color: var(--white); font-weight: 300; letter-spacing: 0.3px;
  }
  .therapist-title {
    position: absolute; left: 559px; top: 391px;
    font-size: 19px; color: var(--gold); font-weight: 300;
  }
  .contact {
    position: absolute; left: 528px; top: 450px;
    font-size: 19px; line-height: 26.5px; color: var(--text-dark); font-weight: 300;
  }

  .brand-name {
    position: absolute; text-align: center; color: var(--silver);
    font-weight: 300; line-height: 1.05; letter-spacing: 1px;
  }
  .brand-front { left: 55px; top: 400px; width: 190px; font-size: 38px; }

  .back-photo {
    position: absolute; inset: 0;
    background:
      radial-gradient(ellipse at 58% 22%, #a98258 0%, #6e5137 28%, rgba(40,30,22,0) 55%),
      radial-gradient(ellipse at 38% 58%, #c79a3e 0%, rgba(160,110,50,0.5) 22%, rgba(0,0,0,0) 45%),
      radial-gradient(ellipse at 60% 78%, #b98a63 0%, rgba(120,80,55,0.4) 30%, rgba(0,0,0,0) 60%),
      linear-gradient(180deg, #2a221c 0%, #1c1713 55%, #3a2a20 100%);
  }
  .brand-back { left: 383px; top: 640px; width: 300px; font-size: 62px; top: 40px; }
</style>
</head>
<body>

<section class="card card-front">
  <div class="front-photo" role="img" aria-label="Beauty portrait in profile with dramatic gold and black eye makeup"></div>

  <svg class="card-shapes" width="966" height="596" viewBox="0 0 966 596" aria-hidden="true">
    <defs>
      <linearGradient id="goldBand" x1="0" y1="0" x2="1" y2="0">
        <stop offset="0" stop-color="var(--gold-deep)" style="stop-color:#b8862a"/>
        <stop offset="0.35" stop-color="#f2d27a"/>
        <stop offset="0.7" stop-color="#e0b451"/>
        <stop offset="1" stop-color="#c28f2c"/>
      </linearGradient>
    </defs>
    <!-- gold band -->
    <path d="M421 440 L966 440 L966 557 L520 557 C470 530 430 490 421 440 Z" fill="url(#goldBand)"/>
    <!-- black band -->
    <path d="M418 346 L966 346 L966 440 L421 440 C414 410 413 378 418 346 Z" fill="#050505"/>
    <!-- white panel -->
    <path d="M432 37 L966 37 L966 346 L418 346 C410 290 440 240 438 170 C437 110 436 70 432 37 Z" fill="#ffffff"/>
    <!-- edge curves -->
    <path d="M418 37 C432 80 432 140 428 190 C420 270 398 320 406 390 C414 470 460 530 528 557"
          fill="none" stroke="#e0aa2e" stroke-width="7"/>
    <path d="M428 37 C440 80 440 140 436 190 C428 270 408 320 414 390 C421 465 465 525 532 553"
          fill="none" stroke="#6f6f6f" stroke-width="3"/>
  </svg>

  <h2 class="services-title">SERVICIOS</h2>
  <ul class="services-list services-left">
    <li>&nbsp;Waxing</li>
    <li>Tinting</li>
    <li>Swedish<span class="wrap">massage</span></li>
    <li>hot stone<span class="wrap">&nbsp;massage</span></li>
    <li>facials</li>
  </ul>
  <ul class="services-list services-right">
    <li>peels</li>
    <li>micro</li>
    <li>LED light treatment</li>
    <li>skin needling and retail</li>
    <li>products Deadline</li>
  </ul>

  <p class="therapist-name">Corinne Halstead Pryce</p>
  <p class="therapist-title">Advanced beauty therapist</p>
  <p class="contact">0455 817 302<br>Lunes - Viernes 9am<br>Fines de semana de 14:30 y noches con cita previa</p>

  <p class="brand-name brand-front">Lumora<br>Beauty</p>
</section>

<section class="card card-back">
  <div class="back-photo" role="img" aria-label="Hot stone massage: client lying on a massage table under a gold towel while a therapist places warm stones on her back"></div>
  <p class="brand-name brand-back">Lumora<br>Beauty</p>
</section>

</body>
</html>
```